Business Card for Amber Heron Advisors

Business card design for Amber Heron Advisors, a new consulting and financial advisory firm. I would like the designs to integrate the logo attached (at least on 1 side).

Target Market(s)

individual and institutional clients

Contact Information for Business Card

Dominic L. Hartwell, CFA
Managing Director
amberheronadvisors.examplep
hartwell@amberheronadvisors.example
(555) 218-4903

```html
<!DOCTYPE html>
<html lang="en">
<head>
<meta charset="utf-8">
<title>Amber Heron Advisors — Business Card</title>
<link rel="stylesheet" href="https://fonts.googleapis.com/css2?family=Jost:wght@400;600&family=League+Spartan:wght@700&display=swap">
<style>
  :root {
    --backdrop: #1f1f1f;
    --card: #2a2d30;
    --amber: #e08a2a;
    --ink-light: #f2f2f2;
    --rule: #e9e9e9;
  }
  * { box-sizing: border-box; margin: 0; padding: 0; }
  html, body {
    width: 1189px; height: 1200px; overflow: hidden;
    background: var(--backdrop);
  }
  .canvas { position: relative; width: 1189px; height: 1200px; }
  .card {
    position: absolute; left: 171px; width: 856px; height: 488px;
    background: var(--card);
  }
  .card--front { top: 67px; }
  .card--back { top: 627px; }

  .brand-name {
    font-family: "Jost", sans-serif; font-weight: 600;
    color: var(--amber); white-space: nowrap; letter-spacing: 0.5px;
  }
  .card--front .brand-name {
    position: absolute; left: 0; right: 0; top: 204px;
    text-align: center; font-size: 54px; line-height: 80px;
  }

  .brand-frame {
    position: absolute; left: 54px; top: 45px; width: 748px; height: 160px;
    border: 2px solid var(--rule);
    display: flex; align-items: center; justify-content: center;
  }
  .card--back .brand-name { font-size: 50px; }

  .holder {
    position: absolute; left: 0; right: 0; top: 244px; text-align: center;
  }
  .holder__name {
    font-family: "League Spartan", sans-serif; font-weight: 700;
    color: var(--amber); font-size: 29px; letter-spacing: 0.6px; line-height: 34px;
  }
  .holder__title {
    font-family: "Jost", sans-serif; font-weight: 400;
    color: var(--ink-light); font-size: 20px; letter-spacing: 0.5px; line-height: 26px;
  }

  .contact-box {
    position: absolute; left: 54px; top: 346px; width: 748px; height: 107px;
    border: 2px solid var(--rule);
    display: flex; flex-direction: column; align-items: center; justify-content: center;
    font-family: "Jost", sans-serif; font-weight: 400;
    color: var(--ink-light); font-size: 20px; line-height: 29px; letter-spacing: 0.3px;
  }
  .contact-box .web-domain { color: var(--amber); }
</style>
</head>
<body>
<main class="canvas">
  <section class="card card--front" aria-label="Card front">
    <p class="brand-name">Amber Heron Advisors</p>
  </section>

  <section class="card card--back" aria-label="Card back">
    <div class="brand-frame">
      <p class="brand-name">Amber Heron Advisors</p>
    </div>
    <div class="holder">
      <p class="holder__name">DOMINIC L. HARTWELL, CFA</p>
      <p class="holder__title">Managing Director</p>
    </div>
    <div class="contact-box">
      <p class="contact-phone">(555) 218-4903</p>
      <p class="contact-email">hartwell@amberheronadvisors.example</p>
      <p class="contact-web"><span class="web-domain">amberheronadvisors</span>.example</p>
    </div>
  </section>
</main>
</body>
</html>
```